IT support company needs Banner Ad for the top of their quote layout template

We need a banner Ad for the top of our for quote layout template so it is sent out on all our quotes

The banner size must be 827 x 100 pixels - anything larger than 60 KB can cause upload time issues

We have attached our logo and examples of the quote page to see how it looks in the context of the whole page.

Essential elements of the banner
- Must have our logo but this can be changed to be different colours if it makes the design work better i.e. Tidal Grove could be all in white

Colours
- Can use all of our standard colours - Orange, Black, Grey and White

Images
- As a premium IT support company we deal with people and technology so would like to see both of these Incorporated into the banner i.e. people using technology These images could be watermarked or one colour effect.

Look and Feel
- Professional, friendly, people, technology, premium

Target Market
Small business owners and managers

Industry/Entity Type

It Company

```html
<!DOCTYPE html>
<html lang="en">
<head>
<meta charset="utf-8">
<title>Tidal Grove – Quote Header Banners</title>
<link rel="stylesheet" href="https://fonts.googleapis.com/css2?family=Michroma&display=swap">
<style>
  :root {
    --stage: #e3e3e3;
    --banner-bg: #ffffff;
    --brand-black: #111111;
    --brand-orange: #ff6a00;
    --photo-light: #cfcfcf;
    --photo-mid: #9a9a9a;
    --photo-dark: #4a4a4a;
    --shadow: rgba(0, 0, 0, 0.45);
  }
  * { margin: 0; padding: 0; box-sizing: border-box; }
  html, body { width: 1200px; height: 1000px; overflow: hidden; }
  body {
    background: var(--stage);
    position: relative;
    font-family: "Michroma", "Arial", sans-serif;
  }
  .banner {
    position: absolute;
    background: var(--banner-bg);
    box-shadow: 2px 3px 5px var(--shadow);
    overflow: hidden;
  }
  .banner--standard { left: 185px; top: 197px; width: 830px; height: 101px; }
  .banner--large    { left: 92px;  top: 388px; width: 1020px; height: 124px; }

  .banner__brand {
    position: absolute;
    display: flex;
    align-items: center;
    height: 100%;
  }
  .banner--standard .banner__brand { left: 44px; gap: 12px; }
  .banner--large .banner__brand    { left: 54px; gap: 15px; }

  .brand__dot {
    flex: none;
    border-radius: 50%;
    background: var(--brand-orange);
  }
  .banner--standard .brand__dot { width: 20px; height: 20px; }
  .banner--large .brand__dot    { width: 25px; height: 25px; }

  .brand__name {
    color: var(--brand-black);
    font-weight: 400;
    white-space: nowrap;
    letter-spacing: 1px;
    line-height: 1;
  }
  .banner--standard .brand__name { font-size: 34px; }
  .banner--large .brand__name    { font-size: 42px; }

  .banner__visual {
    position: absolute;
    top: 0;
    height: 100%;
  }
  .banner--standard .banner__visual { left: 540px; width: 290px; }
  .banner--large .banner__visual    { left: 665px; width: 355px; }
</style>
</head>
<body>

  <section class="banner banner--standard" aria-label="Quote header banner, 827 by 100">
    <div class="banner__brand">
      <span class="brand__dot" aria-hidden="true"></span>
      <span class="brand__name">TIDAL GROVE</span>
    </div>
    <svg class="banner__visual" viewBox="0 0 290 101" preserveAspectRatio="none">
      <defs>
        <linearGradient id="photo-tone-a" x1="0" y1="1" x2="1" y2="0">
          <stop offset="0" stop-color="var(--photo-dark)"/>
          <stop offset="0.55" stop-color="var(--photo-mid)"/>
          <stop offset="1" stop-color="var(--photo-light)"/>
        </linearGradient>
      </defs>
      <path role="img" aria-label="Black and white photo of people at a café table using a laptop and smartphone"
            d="M18,0 Q46,50.5 18,101 H290 V0 Z" fill="url(#photo-tone-a)"/>
      <path class="banner__arc" d="M0,0 Q26,50.5 0,101 H18 Q46,50.5 18,0 Z" fill="var(--brand-orange)"/>
    </svg>
  </section>

  <section class="banner banner--large" aria-label="Quote header banner, large">
    <div class="banner__brand">
      <span class="brand__dot" aria-hidden="true"></span>
      <span class="brand__name">TIDAL GROVE</span>
    </div>
    <svg class="banner__visual" viewBox="0 0 355 124" preserveAspectRatio="none">
      <defs>
        <linearGradient id="photo-tone-b" x1="0" y1="1" x2="1" y2="0">
          <stop offset="0" stop-color="var(--photo-dark)"/>
          <stop offset="0.55" stop-color="var(--photo-mid)"/>
          <stop offset="1" stop-color="var(--photo-light)"/>
        </linearGradient>
      </defs>
      <path role="img" aria-label="Black and white photo of people at a café table using a laptop and smartphone"
            d="M22,0 Q56,62 22,124 H355 V0 Z" fill="url(#photo-tone-b)"/>
      <path class="banner__arc" d="M0,0 Q32,62 0,124 H22 Q56,62 22,0 Z" fill="var(--brand-orange)"/>
    </svg>
  </section>

</body>
</html>
```